Unique Business Card Design

Unique Business Card design for our orthotic and prosthetic company. Our logo is on our website, color is light blue. Unique shape (artificial leg shaped, vertical, etc..) preferred. Logo, business name, individual name and basic demographics needed.

Industry/Entity Type

Business

Contact Information for Business Card

Logo, Industry, Phone # Logo, "Prosthetic & Orthotic Services" Place to add individual name and contact info

Colors
cee9f5

Requirements
Must have
• The icon must be there, placement of "Prosthetic & Orthotic Services" can be moved
Nice to have
• Like the mix of light blue, and a little darker blue. One design included the icons from my website which was a nice touch

```html
<!DOCTYPE html>
<html lang="en">
<head>
<meta charset="utf-8">
<title>Limbwell Inc. – Business Card</title>
<link rel="stylesheet" href="https://fonts.googleapis.com/css2?family=Open+Sans:ital,wght@0,400;0,600;0,700;1,400&display=swap">
<style>
  :root {
    --brand-blue: #2d3596;
    --brand-blue-light: #3640a8;
    --paper: #ffffff;
    --backdrop: #1f1f21;
    --text-soft: #d9dcf3;
  }
  * { box-sizing: border-box; margin: 0; padding: 0; }
  html, body {
    width: 1200px; height: 1000px; overflow: hidden;
    background: var(--backdrop);
    font-family: "Open Sans", Arial, sans-serif;
  }
  .canvas { position: relative; width: 1200px; height: 1000px; }

  .card {
    position: absolute;
    width: 540px; height: 310px;
    border-radius: 26px;
    overflow: hidden;
  }
  .card--back {
    left: 70px; top: 150px;
    background: linear-gradient(135deg, var(--brand-blue-light), var(--brand-blue));
    color: var(--paper);
  }
  .card--front {
    left: 590px; top: 530px;
    background: var(--brand-blue);
  }
  .card__bg { position: absolute; inset: 0; }

  /* Brand block */
  .brand {
    position: absolute;
    display: flex; flex-direction: column; align-items: flex-start;
  }
  .brand__row { display: flex; align-items: center; gap: 10px; }
  .brand__dot {
    width: 58px; height: 58px; border-radius: 50%;
    background: var(--paper);
  }
  .brand__name {
    font-size: 27px; font-weight: 600; letter-spacing: 0.5px;
    line-height: 1;
  }
  .brand__rule {
    width: 220px; height: 2px; margin: 6px 0 4px;
  }
  .brand__tagline {
    font-size: 14px; font-style: italic; font-weight: 400;
  }
  .brand__phone {
    font-size: 34px; font-weight: 700; margin-top: 6px; letter-spacing: 0.5px;
  }

  .card--back .brand { left: 150px; top: 58px; }
  .card--back .brand__rule { background: var(--paper); }
  .card--back .brand__name,
  .card--back .brand__tagline,
  .card--back .brand__phone { color: var(--paper); }

  .site {
    position: absolute; left: 0; right: 0; bottom: 38px;
    display: flex; justify-content: center; align-items: center; gap: 6px;
    font-size: 15px; color: var(--text-soft);
  }
  .site svg { width: 13px; height: 13px; }

  .card--front .brand { left: 34px; top: 98px; }
  .card--front .brand__dot { background: var(--brand-blue); }
  .card--front .brand__rule { background: var(--brand-blue); }
  .card--front .brand__name,
  .card--front .brand__tagline,
  .card--front .brand__phone { color: var(--brand-blue); }

  .person {
    position: absolute; left: 352px; top: 56px;
    color: var(--paper);
  }
  .person__name { font-size: 21px; font-weight: 700; line-height: 1.1; }
  .person__role { font-size: 15px; font-weight: 600; margin-bottom: 12px; }
  .person__address { font-size: 12.5px; color: var(--text-soft); line-height: 1.35; margin-bottom: 10px; }
  .contact { list-style: none; font-size: 12.5px; color: var(--text-soft); }
  .contact li { display: flex; align-items: center; gap: 8px; line-height: 1.55; }
  .contact svg { width: 11px; height: 11px; flex: none; }
</style>
</head>
<body>
<main class="canvas">

  <section class="card card--back" aria-label="Card back">
    <div class="brand">
      <div class="brand__row">
        <span class="brand__dot"></span>
        <span class="brand__name">LIMBWELL INC.</span>
      </div>
      <span class="brand__rule"></span>
      <span class="brand__tagline">Prosthetic &amp; Orthotic Services</span>
      <span class="brand__phone">212.555.0148</span>
    </div>
    <div class="site">
      <svg viewBox="0 0 16 16" fill="none" stroke="currentColor" stroke-width="1.4"><circle cx="8" cy="8" r="6.5"/><ellipse cx="8" cy="8" rx="3" ry="6.5"/><path d="M1.5 8h13M2.5 4.5h11M2.5 11.5h11"/></svg>
      <span>yoursitename.com</span>
    </div>
  </section>

  <section class="card card--front" aria-label="Card front">
    <svg class="card__bg" viewBox="0 0 540 310" preserveAspectRatio="none">
      <path d="M0 0 H268 C330 80 340 200 300 310 H0 Z" fill="var(--paper)"/>
      <path d="M292 0 C354 80 364 200 324 310" fill="none" stroke="var(--paper)" stroke-width="4"/>
      <path d="M278 0 C340 80 350 200 310 310" fill="none" stroke="var(--brand-blue)" stroke-width="6"/>
    </svg>

    <div class="brand">
      <div class="brand__row">
        <span class="brand__dot"></span>
        <span class="brand__name">LIMBWELL INC.</span>
      </div>
      <span class="brand__rule"></span>
      <span class="brand__tagline">Prosthetic &amp; Orthotic Services</span>
      <span class="brand__phone">212.555.0148</span>
    </div>

    <div class="person">
      <p class="person__name">DANIEL REYES</p>
      <p class="person__role">Director</p>
      <p class="person__address">Your Street Address,<br>New York, 1234</p>
      <ul class="contact">
        <li>
          <svg viewBox="0 0 16 16" fill="currentColor"><path d="M3.5 1.5l2.5 0 1 3.5-1.8 1.2a8 8 0 0 0 4.6 4.6L11 9l3.5 1v2.5c0 1-1 2-2 2A11 11 0 0 1 1.5 3.5c0-1 1-2 2-2z"/></svg>
          <span>+000 12345 6789</span>
        </li>
        <li>
          <svg viewBox="0 0 16 16" fill="currentColor"><path d="M1 3h14v10H1z"/><path d="M1 3l7 6 7-6" fill="none" stroke="var(--brand-blue)" stroke-width="1.3"/></svg>
          <span>yourname@email.com</span>
        </li>
        <li>
          <svg viewBox="0 0 16 16" fill="none" stroke="currentColor" stroke-width="1.4"><circle cx="8" cy="8" r="6.5"/><ellipse cx="8" cy="8" rx="3" ry="6.5"/><path d="M1.5 8h13"/></svg>
          <span>www.yoursitename.com</span>
        </li>
      </ul>
    </div>
  </section>

</main>
</body>
</html>
```